依頼詳細
今回SEO対策を行い、遺品整理サービスの集客目的のホームページを作成したいと考えております。
遺品整理をご利用になる方にとって、見やすいホームページ(文字は大きめ)を作成したいと思います。いろいろな年代の方が見ても、どこにボタンがあるのか、どこを押せばよいのか、電話番号はどこにあるのかなどを意識したデザインを希望します。
首都圏はスマホの利用率が高い為、レスポンシブデザインのみやすさも考慮していただきたいと考えております。

今後ますます需要が増える遺品整理サービスを拡大していけるようなホームページにしていきたいと思いっております。

よりよいデザインをしていただけることを希望いたします。

よろしくお願いいたします。

下記のサイトはイメージです。同じにならないようにお願いします。

画像素材等は出来ましたら有料素材画像等を選定いただき、ご提案いただければと思います。素材は弊社にて購入させていただきますので、宜しくお願い申し上げます。
サイトURL
http://www.kumoya-harbor.com/
ページ数
1ページ
希望イメージ
シンプル 複雑
単色 カラフル
暗い 明るい
日常 高級
遊び心 厳粛
未来的 伝統的
女性的 男性的
希望する色
赤系、温かみのある感じが良いです。
納品ファイル
• 高解像度JPG (.jpg)
• イラストレーター形式 (.ai)
• フォトショップ形式 (.psd)
補足説明
レスポンシブデザインを中心にご提案をお願いいたします。
■ 選んだ理由

素晴らしいデザインありがとうございました。今後もデザインコンペを開いていきますのでよろしくお願いいたします。

■ 提案者全員のお礼・コメント

とても温かみのあるデザインありがとうございました。
引き続き修正よろしくお願いいたします。

```html
<!DOCTYPE html>
<html lang="ja">
<head>
<meta charset="utf-8">
<title>(株)クモヤ 遺品整理</title>
<link href="https://fonts.googleapis.com/css2?family=Noto+Sans+JP:wght@400;500;700&family=Noto+Serif+JP:wght@500;700&display=swap" rel="stylesheet">
<style>
:root{
  --orange:#f08a1c;
  --orange-dark:#e07310;
  --green:#8cbf3a;
  --brown:#5a3a22;
  --text:#333;
  --muted:#777;
  --line:#e2d8cc;
  --pale:#f6f3ef;
  --gray:#eeeeee;
  --white:#fff;
}
*{box-sizing:border-box;margin:0;padding:0}
html,body{width:1200px;height:4540px;overflow:hidden}
body{font-family:"Noto Sans JP",sans-serif;color:var(--text);background:var(--white);font-size:15px}
.wrap{width:1000px;margin:0 auto;position:relative}
/* header */
.site-header{height:124px}
.site-header .wrap{display:flex;justify-content:space-between;align-items:center;height:124px}
.brand{display:flex;align-items:center;gap:14px;font-size:40px;font-weight:700;color:var(--brown)}
.brand-dot{width:46px;height:46px;border-radius:50%;background:var(--green)}
.tel-box{text-align:left}
.tel-box small{font-size:16px;font-weight:700;color:var(--text)}
.tel-num{display:flex;align-items:center;gap:8px;font-size:44px;font-weight:700;color:var(--orange);line-height:1.1}
/* nav */
.gnav{background:var(--orange);height:56px}
.gnav ul{display:flex;list-style:none;height:56px;width:1000px;margin:0 auto}
.gnav li{color:#fff;font-size:17px;font-weight:500;padding:0 20px;display:flex;align-items:center;border-right:1px solid rgba(255,255,255,.5)}
.gnav li:first-child{border-left:1px solid rgba(255,255,255,.5)}
/* hero */
.hero{height:440px;position:relative;background:linear-gradient(90deg,#efe4d6 0%,#f8f1e8 45%,#e9ded2 100%)}
.hero-photo{position:absolute;inset:0;background:linear-gradient(100deg,#d9c0a4 0%,#f5ece1 40%,#ece2d8 70%,#c9b8aa 100%)}
.hero-copy{position:absolute;left:180px;top:140px;font-family:"Noto Serif JP",serif;font-size:46px;font-weight:700;color:#3a2a1c;line-height:1.45;text-shadow:0 0 8px #fff}
.hero-copy span{display:block}
.hero-copy span+span{padding-left:46px}
.badge24{position:absolute;left:870px;top:110px;width:100px;height:100px;border-radius:50%;background:var(--green);border:4px solid #fff;color:#fff;text-align:center;font-weight:700;font-size:40px;line-height:1;padding-top:18px}
.badge24 small{display:block;font-size:13px;margin-top:6px}
.hero-btn{position:absolute;left:790px;top:300px;width:290px;height:80px;background:var(--orange);color:#fff;font-size:22px;font-weight:700;display:flex;align-items:center;justify-content:center;border:3px solid #fff;box-shadow:0 3px 8px rgba(0,0,0,.2)}
.hero-band{height:28px;background:linear-gradient(#e0d6cb,#f3eee8)}
/* columns */
.columns{display:flex;justify-content:space-between;padding-top:52px;height:2660px}
.side{width:220px}
.side-box{border:1px solid var(--line);margin-bottom:40px;background:#fff}
.side-box h3{background:var(--brown);color:#fff;text-align:center;font-size:18px;padding:14px 0}
.side-box ul{list-style:none;padding:6px 14px 14px}
.side-box li{color:var(--orange);font-size:17px;line-height:1.5;padding:10px 0 10px 18px;border-bottom:1px dotted var(--line);position:relative;font-weight:500}
.side-box li::before{content:"・";position:absolute;left:0}
.main{width:640px}
.promo{height:220px;display:flex;border:1px solid var(--line)}
.promo-text{width:260px;padding:40px 20px;background:#fff;font-family:"Noto Serif JP",serif}
.promo-text h2{font-size:30px;color:var(--brown);line-height:1.35;border-left:5px solid var(--green);padding-left:14px}
.promo-text p{font-size:15px;margin-top:16px;border-top:1px solid var(--line);padding-top:10px}
.promo-photo{flex:1;background:linear-gradient(120deg,#d8e3c5,#f3efe6 60%,#dccbb5)}
.sec-title{font-size:24px;font-weight:700;color:var(--brown);border-left:8px solid var(--brown);padding-left:14px;line-height:1.3;margin:0 0 20px}
.main .sec-title{margin-top:68px}
.body-text{font-size:15px;line-height:2;color:#555}
.faq-item{padding:30px 0 40px;border-bottom:1px dashed #ccc}
.faq-row{display:flex;gap:16px;align-items:flex-start}
.faq-mark{font-family:"Noto Serif JP",serif;font-size:30px;font-weight:700;line-height:1}
.faq-mark.q{color:var(--green)}
.faq-mark.a{color:var(--orange)}
.faq-row p{font-size:15px;line-height:1.9;color:#555;padding-top:2px}
.faq-row.answer{background:var(--pale);padding:28px 20px;margin-top:26px}
/* cases */
.cases{background:var(--gray);height:560px;padding-top:40px}
.cases-grid{display:grid;grid-template-columns:490px 490px;gap:20px;margin-top:40px}
.case-card{height:200px;border:4px solid #fff;box-shadow:0 2px 6px rgba(0,0,0,.15);background:linear-gradient(135deg,#dcd3c8,#f6f2ec 50%,#c8bcaf);display:flex;align-items:center;justify-content:center}
.case-card span{font-family:"Noto Serif JP",serif;font-size:34px;font-weight:700;color:#4b3a2d;background:rgba(255,255,255,.75);padding:8px 22px}
/* news */
.news{padding-top:100px;height:460px}
.news-list{list-style:none;margin-top:24px}
.news-list li{display:flex;align-items:center;gap:40px;height:80px;border-bottom:1px dotted #ccc;font-size:16px}
.news-list li a{color:var(--orange);text-decoration:none;flex:1}
.arrow{width:18px;height:18px;border-radius:50%;background:var(--orange);position:relative}
.arrow::after{content:"";position:absolute;left:5px;top:5px;border-left:7px solid #fff;border-top:4px solid transparent;border-bottom:4px solid transparent}
.news-more{text-align:right;font-size:13px;color:var(--orange);margin-top:20px}
/* company */
.company{background:var(--gray);height:480px;padding-top:30px}
.company-body{display:flex;gap:40px;margin-top:30px}
.map{width:460px;height:320px;background:linear-gradient(135deg,#eceae6,#dcdad5);border:1px solid #ccc}
.company-info{padding-top:20px}
.company-info .brand{font-size:42px}
.company-info address{font-style:normal;font-size:16px;margin:6px 0 0 60px}
.company-info hr{border:0;border-top:1px solid #ccc;margin:24px 0}
.company-info .tel-num{font-size:50px}
.fax{font-size:26px;font-weight:700;color:var(--orange);margin-left:46px}
/* footer */
.fnav{background:var(--orange);height:60px;margin-top:0}
.fnav ul{justify-content:center}
.copyright{text-align:center;font-size:13px;color:#555;padding-top:16px}
</style>
</head>
<body>
<header class="site-header">
  <div class="wrap">
    <div class="brand"><span class="brand-dot"></span>(株)クモヤ</div>
    <div class="tel-box">
      <small>お電話での問合せ 受付[9:00〜17:00]</small>
      <div class="tel-num">
        <svg width="34" height="34" viewBox="0 0 24 24"><circle cx="12" cy="12" r="12" fill="#f08a1c"/><path d="M8 6l2 3-1.5 1.5a8 8 0 004 4L14 13l3 2-1 2c-5 0-9-4-9-9z" fill="#fff"/></svg>
        048-555-0187
      </div>
    </div>
  </div>
</header>
<nav class="gnav">
  <ul><li>HOME</li><li>遺品整理</li><li>遺品整理の流れ</li><li>よくある質問</li><li>遺品整理事例</li><li>会社情報</li><li>お問合せ</li></ul>
</nav>
<section class="hero">
  <div class="hero-photo" role="img" aria-label="明るい室内と花、ヘッドセットを付けた受付スタッフの写真"></div>
  <h1 class="hero-copy"><span>遺品を気持ちをこめて</span><span>大事にお片付けいたします。</span></h1>
  <div class="badge24">24<small>時間受付</small></div>
  <div class="hero-btn">お問合せはこちら</div>
</section>
<div class="hero-band"></div>

<div class="wrap columns">
  <aside class="side">
    <div class="side-box">
      <h3>遺品整理事例</h3>
      <ul><li>戸田市介護施設　A様</li><li>蕨市介護施設　C様</li><li>さいたま市介護施設 F様</li><li>戸田市介護施設　G様</li><li>さいたま市介護施設 H様</li></ul>
    </div>
    <div class="side-box">
      <h3>よくある質問</h3>
      <ul><li>テキストテキスト？</li><li>テキストテキスト？</li><li>テキストテキストテキストテキスト？</li><li>テキストテキスト？</li><li>テキストテキストテキストテキスト？</li></ul>
    </div>
  </aside>
  <main class="main">
    <div class="promo">
      <div class="promo-text"><h2>クモヤの<br>こだわり</h2><p>遺品整理でお困りの方へ</p></div>
      <div class="promo-photo" role="img" aria-label="車椅子の高齢者に付き添う介護スタッフの写真"></div>
    </div>
    <h2 class="sec-title">遺品整理について</h2>
    <p class="body-text">テキストテキストテキストテキストテキストテキストテキストテキストテキストテキストテキストテキストテキストテキストテキストテキストテキストテキストテキストテキストテキストテキストテキストテキストテキストテキストテキストテキストテキストテキストテキストテキストテキストテキストテキストテキストテキストテキストテキスト</p>
    <h2 class="sec-title">遺品整理の流れ</h2>
    <p class="body-text">テキストテキストテキストテキストテキストテキストテキストテキストテキストテキストテキストテキストテキストテキストテキストテキストテキストテキストテキストテキストテキストテキストテキストテキストテキストテキストテキストテキストテキストテキストテキストテキストテキストテキストテキストテキストテキストテキスト</p>
    <h2 class="sec-title">遺品整理のよくある質問</h2>
    <div class="faq-item">
      <div class="faq-row"><span class="faq-mark q">Q.</span><p>テキストテキストテキストテキストテキストテキストテキストテキストテキストテキストテキストテキストテキストテキスト</p></div>
      <div class="faq-row answer"><span class="faq-mark a">A.</span><p>テキストテキストテキストテキストテキストテキストテキストテキストテキストテキストテキストテキストテキストテキストテキストテキストテキストテキスト</p></div>
    </div>
    <div class="faq-item">
      <div class="faq-row"><span class="faq-mark q">Q.</span><p>テキストテキストテキストテキストテキストテキストテキストテキストテキストテキストテキストテキストテキストテキスト</p></div>
      <div class="faq-row answer"><span class="faq-mark a">A.</span><p>テキストテキストテキストテキストテキストテキストテキストテキストテキストテキストテキストテキストテキストテキストテキストテキストテキストテキスト</p></div>
    </div>
    <div class="faq-item">
      <div class="faq-row"><span class="faq-mark q">Q.</span><p>テキストテキストテキストテキストテキストテキストテキストテキストテキストテキストテキストテキストテキストテキスト</p></div>
      <div class="faq-row answer"><span class="faq-mark a">A.</span><p>テキストテキストテキストテキストテキストテキストテキストテキストテキストテキストテキストテキストテキストテキストテキストテキストテキストテキスト</p></div>
    </div>
  </main>
</div>

<section class="cases">
  <div class="wrap">
    <h2 class="sec-title">遺品整理事例</h2>
    <div class="cases-grid">
      <div class="case-card" role="img" aria-label="整理後の施設の部屋の写真"><span>事例紹介</span></div>
      <div class="case-card" role="img" aria-label="整理後の施設の部屋の写真"><span>事例紹介</span></div>
      <div class="case-card" role="img" aria-label="整理後の施設の部屋の写真"><span>事例紹介</span></div>
      <div class="case-card" role="img" aria-label="整理後の施設の部屋の写真"><span>事例紹介</span></div>
    </div>
  </div>
</section>

<section class="news">
  <div class="wrap">
    <h2 class="sec-title">新着情報</h2>
    <ul class="news-list">
      <li><span>18.02.01</span><a>ホームページを公開しました。</a><span class="arrow"></span></li>
      <li><span>18.02.01</span><a>ホームページを公開しました。</a><span class="arrow"></span></li>
      <li><span>18.02.01</span><a>ホームページを公開しました。</a><span class="arrow"></span></li>
    </ul>
    <p class="news-more">新着情報一覧 ▶</p>
  </div>
</section>

<section class="company">
  <div class="wrap">
    <h2 class="sec-title">企業情報・アクセス</h2>
    <div class="company-body">
      <div class="map" role="img" aria-label="事務所周辺の地図"></div>
      <div class="company-info">
        <div class="brand"><span class="brand-dot"></span>(株)クモヤ</div>
        <address>埼玉県戸田市中町2-8-5</address>
        <hr>
        <small style="font-size:20px;font-weight:700">お電話での問合せ 受付[9:00〜17:00]</small>
        <div class="tel-num">
          <svg width="38" height="38" viewBox="0 0 24 24"><circle cx="12" cy="12" r="12" fill="#f08a1c"/><path d="M8 6l2 3-1.5 1.5a8 8 0 004 4L14 13l3 2-1 2c-5 0-9-4-9-9z" fill="#fff"/></svg>
          048-555-0187
        </div>
        <p class="fax">FAX:048-555-0188</p>
      </div>
    </div>
  </div>
</section>

<footer>
  <nav class="gnav fnav">
    <ul><li>HOME</li><li>遺品整理</li><li>遺品整理の流れ</li><li>よくある質問</li><li>遺品整理事例</li><li>会社情報</li><li>お問合せ</li></ul>
  </nav>
  <p class="copyright">Copyright(C)2018 遺品整理のクモヤ 埼玉県戸田市 All Rights Reserved.</p>
</footer>
</body>
</html>
```